AMBER HARBOUR WEB

We need a home design in wordpress, we have now a web but we would like to improve it. Our current web is www.amberharbourvillas.example Our business is holliday rental of villas in Ibiza. Our guest must know that we are a reliable company, professional and with experience and good reviews. We want them to click in our reservation engine: https://bookings.amberharbourvillas.example/en/ and make reservation in our website. We would also like to say that all the properties that we have are just us who commercialize so we have best price available. Many people are going to see our villas in staylodgr.example and look to our website to make a reservation with us so we need to show them that they are at the right place and click at our link to our reservation engine. What make us special is that we are a local company, we are from Ibiza, Our guests are always received in person by the Amber Harbour Villas team. You will enjoy extensive tourist information when you check in and during the entire stay. You will be attended by ChatPelt and calls, always happy to help so that you have a happy and fun stay! Our guest stay is better than in hotel as they have more spece, private swiming pool, private garden, barbeque ... To rent a villa is the best way to stay in Ibiza. We also have a promotional video: https://vidshare.example/Qm7pTz3RxLa Let our philosophy be shown, we think that coming on holiday to Ibiza implies seeing the nature that we have in Ibiza, hence our name AMBER HARBOUR, like the pins that almost touch the sea in Ibiza, or the posidonea meadows where the intense green of the seaweed and the blue of the sea. We are aware of the environment, and we love Ibiza. For us, the client who visits Ibiza, should rent a car, go around the island, eat in a restaurant one day in front of the sea, is a night of partying to the discs, go shopping, visit the ancient heritage of Umanity, make some aquatic sport, enjoy the pool, those are for us Ibiza.

Target Market(s)

Europe, people from Holand, UK, Germany, France, Spain ...

Industry/Entity Type

Tourism

Colors

Designer to choose colors to be used in the design.

Requirements
Must have
• Pictures of Ibiza.
Nice to have
• Our name Amber Harbour Villas is beacuse in Ibiza there is forest that almost touch the watter of the Mediterranean sea, so you can see green of the forest and blue of the sea and the sky. And also beacause under the watter of the sea there is a plant called Posidonia that is also green please see the picture of posidonia.

```html
<!DOCTYPE html>
<html lang="en">
<head>
<meta charset="utf-8">
<title>Amber Harbour Villas – Home</title>
<link href="https://fonts.googleapis.com/css2?family=Playfair+Display:ital,wght@0,400;0,700;1,400&family=Open+Sans:wght@400;600;700&display=swap" rel="stylesheet">
<style>
:root{
  --green:#8cc63e;
  --green-dark:#76ad2c;
  --cyan:#16a8c8;
  --ink:#2f2f2f;
  --text:#6f6f6f;
  --muted:#9a9a9a;
  --light:#f4f4f4;
  --white:#ffffff;
  --footer:#2a2a2a;
  --footer-bottom:#f1f1f1;
  --serif:'Playfair Display', Georgia, serif;
  --sans:'Open Sans', Arial, sans-serif;
}
*{box-sizing:border-box;margin:0;padding:0}
html,body{width:1200px;height:4088px;overflow:hidden}
body{font-family:var(--sans);color:var(--text);background:var(--white);position:relative}
.eyebrow{font-size:10px;letter-spacing:3px;text-transform:uppercase;color:var(--green);font-weight:600}
.title{font-family:var(--serif);color:var(--ink);font-weight:400}
.copy{font-size:12px;line-height:1.75;color:var(--text)}
.btn{display:inline-block;background:var(--green);color:var(--white);font-size:10px;font-weight:700;letter-spacing:1.5px;text-transform:uppercase;padding:9px 20px}
.photo{position:absolute}

/* header */
.site-header{position:absolute;top:0;left:0;width:1200px;height:56px;background:var(--white);display:flex;align-items:center}
.brand{display:flex;align-items:center;gap:10px;margin-left:22px}
.brand-mark{width:18px;height:18px;border-radius:50%;background:var(--green)}
.brand-name{font-family:var(--serif);font-size:15px;color:var(--green-dark);letter-spacing:1px}
.main-nav{display:flex;gap:28px;margin-left:150px}
.main-nav a{font-size:10px;font-weight:600;letter-spacing:1px;color:var(--ink);text-decoration:none;text-transform:uppercase}
.main-nav a.active{color:var(--cyan)}
.lang{margin-left:auto;font-size:10px;font-weight:600;color:var(--ink);margin-right:24px}
.header-book{width:120px;height:56px;background:var(--green);color:var(--white);font-size:11px;font-weight:700;letter-spacing:1.5px;display:flex;align-items:center;justify-content:center}

/* hero */
.hero{position:absolute;top:56px;left:0;width:1200px;height:604px;background:linear-gradient(180deg,#4d86b8 0%,#2f6f9e 35%,#1d6b86 55%,#4d7d4a 78%,#c9b58d 100%)}
.hero-content{position:absolute;left:0;right:0;top:335px;text-align:center;color:var(--white)}
.hero-content .eyebrow{color:var(--white)}
.hero-content h1{font-family:var(--serif);font-weight:400;font-size:38px;margin:12px 0 24px}

/* intro */
.intro{position:absolute;top:660px;left:0;width:1200px;height:332px;background:var(--light);text-align:center;padding-top:50px}
.intro h2{font-size:32px;margin:10px 0 16px}
.intro .copy{width:500px;margin:0 auto}
.intro .sign{width:90px;height:28px;margin:18px auto 0;background:#e4e4e4}

/* split features */
.feature{position:absolute;left:0;width:1200px;height:408px;background:var(--white)}
.feature .text{position:absolute;top:0;width:400px;height:100%;padding:0 48px;display:flex;flex-direction:column;justify-content:center}
.feature .title{font-size:30px;margin:8px 0 16px}
.feature .copy{margin-bottom:18px}
.feature .btn{align-self:flex-start}
.feature .text.right{text-align:right}
.feature .text.right .btn{align-self:flex-end}

/* cards */
.cards{position:absolute;top:2220px;left:0;width:1200px;height:400px;display:flex}
.card{position:relative;width:400px;height:400px}
.card-box{position:absolute;left:90px;top:60px;width:220px;height:280px;background:rgba(255,255,255,.9);text-align:center;padding:40px 22px}
.card-box.dark{background:rgba(30,30,30,.65)}
.card-box.dark .title,.card-box.dark .copy,.card-box.dark .more{color:var(--white)}
.card .title{font-size:26px;line-height:1.15;margin-bottom:14px}
.card .copy{font-size:11px;margin-bottom:16px}
.more{font-size:9px;font-weight:700;letter-spacing:1.5px;color:var(--ink)}

/* testimonial */
.testimonial{position:absolute;top:2620px;left:0;width:1200px;height:320px;background:linear-gradient(180deg,#3e3a33 0%,#6b5e45 50%,#3a3630 100%);text-align:center;color:var(--white);padding-top:92px}
.stars{display:flex;gap:6px;justify-content:center;margin-bottom:20px}
.stars span{width:8px;height:8px;background:var(--green);transform:rotate(45deg)}
.testimonial blockquote{font-family:var(--serif);font-style:italic;font-size:20px;line-height:1.6;width:700px;margin:0 auto 16px}
.testimonial cite{font-style:normal;font-size:10px;letter-spacing:2px;color:var(--green);text-transform:uppercase}

/* tours */
.tours-grid{position:absolute;top:2940px;left:0;width:800px;height:400px;display:grid;grid-template-columns:repeat(4,1fr);grid-template-rows:repeat(3,1fr)}
.tours-grid div:nth-child(odd){background:linear-gradient(135deg,#1fa3c6,#6ac6d8)}
.tours-grid div:nth-child(even){background:linear-gradient(135deg,#2c7fb0,#e2a84a)}
.tours-grid div:nth-child(4n+3){background:linear-gradient(135deg,#e9d24b,#1f8fbd)}

/* newsletter + news */
.newsletter{position:absolute;top:3340px;left:0;width:400px;height:420px;background:var(--cyan);color:var(--white);padding:110px 48px 0}
.newsletter .eyebrow{color:var(--white)}
.newsletter h3{font-family:var(--serif);font-weight:400;font-size:30px;margin:8px 0 10px}
.newsletter p{font-size:11px;margin-bottom:14px}
.signup{display:flex}
.signup span{width:200px;height:30px;background:var(--white);font-size:10px;color:var(--muted);padding:9px 10px}
.signup b{width:60px;height:30px;background:var(--green);font-size:9px;display:flex;align-items:center;justify-content:center;letter-spacing:1px}
.news{position:absolute;top:3340px;left:400px;width:800px;height:420px;background:var(--light);text-align:center;padding-top:60px}
.news h3{font-size:30px;margin:6px 0 28px}
.news-list{display:flex;gap:24px;justify-content:center}
.news-item{width:250px;background:var(--white);text-align:left;padding:22px 22px 20px;display:flex;gap:14px}
.news-date{font-family:var(--serif);font-size:22px;color:var(--green);line-height:1}
.news-date small{display:block;font-family:var(--sans);font-size:9px;color:var(--muted);letter-spacing:1px}
.news-item h4{font-family:var(--serif);font-weight:400;font-size:14px;color:var(--ink);margin-bottom:6px}
.news-item p{font-size:10px;line-height:1.6;margin-bottom:8px}
.news .btn{margin-top:28px}

/* footer */
.site-footer{position:absolute;top:3760px;left:0;width:1200px;height:200px;background:var(--footer);display:flex;justify-content:space-around;text-align:center;padding-top:52px;color:#bdbdbd}
.foot-col h5{font-family:var(--serif);font-weight:400;font-size:16px;color:var(--white);margin-bottom:12px}
.foot-col p{font-size:11px;line-height:1.7}
.foot-col .btn{margin-top:10px;padding:6px 14px;font-size:9px}
.socials{display:flex;gap:8px;justify-content:center}
.socials span{width:24px;height:24px;border-radius:50%;background:#4a4a4a}
.bottom-bar{position:absolute;top:3960px;left:0;width:1200px;height:128px;background:var(--footer-bottom);font-size:10px;color:var(--muted)}
.bottom-links{position:absolute;left:30px;top:30px;display:flex;gap:14px}
.badges{position:absolute;right:30px;top:22px;display:flex;gap:12px}
.badges span{width:28px;height:28px;border-radius:50%;background:#d2d2d2}
.copyright{position:absolute;left:0;right:0;top:76px;text-align:center}
</style>
</head>
<body>

<header class="site-header">
  <div class="brand"><span class="brand-mark"></span><span class="brand-name">AMBER HARBOUR</span></div>
  <nav class="main-nav">
    <a class="active" href="#">Home</a>
    <a href="#">Villas and Countryside</a>
    <a href="#">Restaurant</a>
    <a href="#">Experience</a>
    <a href="#">About Us</a>
    <a href="#">Contact Us</a>
  </nav>
  <span class="lang">EN</span>
  <div class="header-book">BOOK NOW</div>
</header>

<section class="hero" role="img" aria-label="Ibiza cove with pine forest reaching turquoise sea, sailboats and a sandy beach">
  <div class="hero-content">
    <div class="eyebrow">Welcome to Amber Harbour Villas Ibiza</div>
    <h1>Comfortable Villas &amp; Countryside</h1>
    <span class="btn">Book Now</span>
  </div>
</section>

<section class="intro">
  <div class="eyebrow">Welcome to Amber Harbour Villas</div>
  <h2 class="title">A New Vision of Luxury</h2>
  <p class="copy">We are a local Ibiza family company offering private villas with pool, garden and barbecue. Every guest is welcomed in person, receives full island tips on arrival and can reach our team by chat or phone for the whole stay, always at the best direct price.</p>
  <div class="sign" role="img" aria-label="Handwritten signature of the owner"></div>
</section>

<section class="feature" style="top:992px">
  <div class="text" style="left:0">
    <div class="eyebrow">Accommodation</div>
    <h3 class="title">Villas &amp; Countryside</h3>
    <p class="copy">Spacious private villas surrounded by pine forest, each with its own pool and garden, rented only through us at the best price.</p>
    <span class="btn">Read More</span>
  </div>
  <div class="photo" role="img" aria-label="Bright villa living room with wooden beams, sofas and open doors" style="left:400px;top:0;width:800px;height:408px;background:linear-gradient(120deg,#b08458 0%,#d9c3a3 35%,#efe6d6 60%,#cdb893 100%)"></div>
</section>

<section class="feature" style="top:1400px;height:400px">
  <div class="photo" role="img" aria-label="White villa with blue swimming pool, loungers and palm trees" style="left:0;top:0;width:800px;height:400px;background:linear-gradient(180deg,#6aa6dc 0%,#e9ecef 40%,#4c8a4a 55%,#2d9fd6 80%,#4fc0e6 100%)"></div>
  <div class="text right" style="left:800px">
    <div class="eyebrow">Natural Relax</div>
    <h3 class="title">Wellness &amp; Spa</h3>
    <p class="copy">Unwind by your private pool, book a massage at the villa and enjoy the calm of the Ibiza countryside.</p>
    <span class="btn">Read More</span>
  </div>
</section>

<section class="feature" style="top:1800px;height:420px">
  <div class="text" style="left:0">
    <div class="eyebrow">Taste of Ibiza</div>
    <h3 class="title">Restaurants &amp; Bars</h3>
    <p class="copy">Our favourite tables by the sea, from fresh fish lunches to sunset cocktails, chosen by our local team.</p>
    <span class="btn">Read More</span>
  </div>
  <div class="photo" role="img" aria-label="Seafront restaurant terrace with white tables facing a rocky bay" style="left:400px;top:0;width:800px;height:420px;background:linear-gradient(180deg,#8fc3e6 0%,#2f8fb8 45%,#e6eef2 70%,#bfc9cf 100%)"></div>
</section>

<section class="cards">
  <div class="card" role="img" aria-label="Pool terrace at dusk" style="background:linear-gradient(160deg,#2a8ec2,#7cc6e6)">
    <div class="card-box">
      <h3 class="title">Offers &amp; Packages</h3>
      <p class="copy">Seasonal deals and long stay discounts booked direct.</p>
      <span class="more">LEARN MORE</span>
    </div>
  </div>
  <div class="card" role="img" aria-label="Colourful boutique shop with summer clothes" style="background:linear-gradient(160deg,#e85a8a,#f1c27a)">
    <div class="card-box">
      <h3 class="title">Shopping</h3>
      <p class="copy">Hippy markets, local crafts and island boutiques to visit.</p>
      <span class="more">LEARN MORE</span>
    </div>
  </div>
  <div class="card" role="img" aria-label="Elegant dining table set with glasses" style="background:linear-gradient(160deg,#3a3a3a,#8c8c8c)">
    <div class="card-box dark">
      <h3 class="title">Concierge &amp; Services</h3>
      <p class="copy">Car hire, chefs, boats and tickets arranged for you.</p>
      <span class="more">LEARN MORE</span>
    </div>
  </div>
</section>

<section class="testimonial" role="img" aria-label="Friends on the beach at sunset">
  <div class="stars"><span></span><span></span><span></span><span></span><span></span></div>
  <blockquote>“Pool – check, Accommodation – check, Beauty – check. Yes! I think this could be the most perfect place to be in the world!”</blockquote>
  <cite>Helena Marsh, London, UK</cite>
</section>

<div class="tours-grid" role="img" aria-label="Collage of water sports: jet skis, parasailing, banana boats, snorkelling and paddle boarding">
  <div></div><div></div><div></div><div></div><div></div><div></div>
  <div></div><div></div><div></div><div></div><div></div><div></div>
</div>
<section class="feature" style="top:2940px;left:800px;width:400px;height:400px">
  <div class="text right" style="left:0">
    <div class="eyebrow">Our Recommendations</div>
    <h3 class="title">Tours &amp; Excursions</h3>
    <p class="copy">Boat trips, water sports, island tours and heritage visits, the real Ibiza our team loves.</p>
    <span class="btn">Read More</span>
  </div>
</section>

<section class="newsletter">
  <div class="eyebrow">Subscribe Now</div>
  <h3>Newsletter Sign Up</h3>
  <p>Sign up to receive our latest offers.</p>
  <div class="signup"><span>Your email address</span><b>SEND</b></div>
</section>

<section class="news">
  <div class="eyebrow">What's New</div>
  <h3 class="title">The News</h3>
  <div class="news-list">
    <article class="news-item">
      <div class="news-date">12<small>JUN</small></div>
      <div>
        <h4>Summer Nights by the Sea</h4>
        <p>Our pick of beach bars for the best sunsets on the west coast.</p>
        <span class="more">READ MORE</span>
      </div>
    </article>
    <article class="news-item">
      <div class="news-date">04<small>MAY</small></div>
      <div>
        <h4>Posidonia Meadows</h4>
        <p>Why the green seagrass keeps the island water so clear.</p>
        <span class="more">READ MORE</span>
      </div>
    </article>
  </div>
  <span class="btn">View All</span>
</section>

<footer class="site-footer">
  <div class="foot-col">
    <h5>Call Us</h5>
    <p>+34 971 555 018<br>Mon – Sun 9:00 – 21:00</p>
  </div>
  <div class="foot-col">
    <h5>Our Location</h5>
    <p>Carrer del Moll 12<br>07820 Sant Antoni, Ibiza</p>
    <span class="btn">Get Directions</span>
  </div>
  <div class="foot-col">
    <h5>Email Us</h5>
    <p>hello@amberharbourvillas.example</p>
    <span class="btn">Send Message</span>
  </div>
  <div class="foot-col">
    <h5>Stay Connected</h5>
    <div class="socials"><span></span><span></span><span></span><span></span></div>
  </div>
</footer>

<div class="bottom-bar">
  <div class="bottom-links"><span>Home</span><span>Privacy Policy</span><span>Terms</span><span>Contact Us</span></div>
  <div class="badges"><span></span><span></span><span></span><span></span><span></span><span></span></div>
  <div class="copyright">© 2024 Amber Harbour Villas. All rights reserved.</div>
</div>

</body>
</html>
```